Advertisement for Fresh Horizons Award 2019 needed

I am Lobbying for the needs of youngsters in a specific region. This year I am planning the first fresh horizons award to give young people the chance to present their regional projekts/activities/initiatives and to award them some price money they can use for further activites. This Initiative is not only targeted at young people but also organizations who work with youngsters. Therefore I would need an advertisment we could use to promote this event in newspapers, website and via an E-Mail Campaign. Possibly also on social media, so I am thinking of a Facebook and Instagram Design as well. I uploaded some logos and materials that we are using already. to give you an idea of the colors. The ad should be targeted towards a young audience but also draw the attention of people who work with youngsters. Size MAX. (length x width) 21cm x 7cm
Youngsters age 14-26 yrs
People who work with youngsters (youth organizations, schools, clubs, social workers, municipalities)

```html
<!DOCTYPE html>
<html lang="de">
<head>
<meta charset="utf-8">
<title>Fresh Horizons Award 2019</title>
<link rel="stylesheet" href="https://fonts.googleapis.com/css2?family=Oswald:wght@700&family=Roboto+Condensed:wght@400;700&display=swap">
<style>
  :root {
    --frame-blue: #1d8bc6;
    --frame-blue-dark: #15679a;
    --panel-black: #000000;
    --brand-white: #ffffff;
    --title-yellow: #ffe600;
    --tagline-orange: #f08a00;
    --info-green: #5cb531;
    --date-red: #e30613;
    --time-yellow: #ffe600;
    --visual-light: #ececf0;
    --visual-tone: #b9a7d6;
  }
  html, body {
    margin: 0;
    padding: 0;
    width: 1200px;
    height: 400px;
    overflow: hidden;
    background: #ffffff;
  }
  .banner {
    position: relative;
    width: 1200px;
    height: 400px;
    background: linear-gradient(135deg, var(--frame-blue) 0%, var(--frame-blue-dark) 50%, var(--frame-blue) 100%);
    overflow: hidden;
  }
  .info-panel {
    position: absolute;
    left: 18px;
    top: 18px;
    width: 724px;
    height: 364px;
    background: var(--panel-black);
    text-align: center;
    font-family: "Roboto Condensed", "Arial Narrow", sans-serif;
  }
  .brand {
    position: absolute;
    left: 0;
    right: 0;
    top: 72px;
    height: 28px;
    display: flex;
    justify-content: center;
    align-items: center;
    gap: 14px;
    color: var(--brand-white);
    font-weight: 400;
    font-size: 22px;
    letter-spacing: 5px;
    text-transform: uppercase;
  }
  .brand-dot {
    width: 14px;
    height: 14px;
    border-radius: 50%;
    background: var(--brand-white);
  }
  .award-title {
    position: absolute;
    left: 0;
    right: 0;
    top: 105px;
    margin: 0;
    font-family: "Oswald", Impact, sans-serif;
    font-weight: 700;
    font-size: 44px;
    line-height: 50px;
    letter-spacing: 2px;
    color: var(--title-yellow);
    text-transform: uppercase;
  }
  .tagline {
    position: absolute;
    left: 0;
    right: 0;
    top: 158px;
    margin: 0;
    font-size: 28px;
    line-height: 32px;
    color: var(--tagline-orange);
  }
  .eligibility {
    position: absolute;
    left: 0;
    right: 0;
    top: 197px;
    margin: 0;
    font-size: 26px;
    line-height: 33px;
    color: var(--info-green);
  }
  .schedule {
    position: absolute;
    left: 50px;
    top: 306px;
    width: 624px;
    height: 36px;
  }
  .schedule-date,
  .schedule-time {
    position: absolute;
    top: 0;
    height: 36px;
    line-height: 36px;
    border-radius: 18px;
    font-weight: 700;
    font-size: 26px;
    box-sizing: border-box;
    white-space: nowrap;
  }
  .schedule-time {
    left: 340px;
    width: 284px;
    background: var(--time-yellow);
    color: var(--date-red);
    text-align: right;
    padding-right: 14px;
  }
  .schedule-date {
    left: 0;
    width: 352px;
    background: var(--date-red);
    color: var(--title-yellow);
    border: 2px solid var(--panel-black);
    line-height: 32px;
  }
  .visual-panel {
    position: absolute;
    left: 742px;
    top: 18px;
    width: 440px;
    height: 364px;
    background: linear-gradient(160deg, var(--visual-light) 0%, var(--visual-tone) 100%);
  }
</style>
</head>
<body>
  <div class="banner">
    <section class="info-panel">
      <div class="brand"><span class="brand-dot"></span>Hügelland Region</div>
      <h1 class="award-title">Fresh Horizons Award 2019</h1>
      <p class="tagline">ein regionaler Preis für innovative Jugendprojekte</p>
      <p class="eligibility">
        einreichen können Jugendliche zwischen 12 und 26 Jahren,<br>
        VertreterInnen von Gemeinden, Institutionen,<br>
        Verbänden und Vereinen
      </p>
      <div class="schedule">
        <div class="schedule-time">von 17:00 - 20:00 Uhr</div>
        <div class="schedule-date">Donnerstag, 19. September</div>
      </div>
    </section>
    <div class="visual-panel" role="img" aria-label="Silhouettes of jumping young people in front of colourful bubbles"></div>
  </div>
</body>
</html>
```